Complete web site needs re-design

Webpage will include one product labeled Talvex (™) .
This webpage must be viewable on Mobile devices and all common browsers - Safari, Chrome, IE, Mozilla Firefox..

Design will be similar to that of
http://www.morvellworks.example/aviation/
or
http://www.plexory.example/site-layout/view/html/482?utm_content=qx_html_ktp_demo_3_7TrialItem&utm_medium=layout_strip&utm_campaign=qx_ktp&utm_source=opensitelayouts&experiment_id=qx_html_ktp_demo_3_7TrialItem&utm_term=meetups

- in that it will be simple and introduce our product.

Website will be ready to accept shop till when the product is released. The integration of this feature will also go to the winner.

Tabs for information will be provided for "About, Features, Where to buy"

The page should include one vidqueue as a sample of the product. this will be linked to the following video http://www.vidqueue.example/watch?v=kRT519pz8va.

Good luck applicants!

Target Market(s)

The target audience will be sport enthusiasts of all walks (from car racing to skydiving) looking to supplement their zip-cam camera with an extra mount.

Industry/Entity Type

Events

Font styles to use
Other font styles liked:
• Helvetica

Colors
d5d5d5
919191
f6f6f6
c8c8c8
ebebeb
5c5c5c
aaaaaa
ffffff

Requirements
Must have
• Front page is introducing our "Talvex" product. Search engines need to identify "Extreme, POV, ZipCam, Self,Levelling, Auto, Stabilising, Motocross, surfing, Moto X, Wake, Kite, Boarding, Skydiving, Racing, Bike, Aerobatic, blue stag, Mount,Ski, downhill, snow, base jumping," etc..

The mount is designed to hold a zip-cam camera in all and any extreme situations. Ensure the search returns this .

An "about" and "contact" shall be provided on the company logo.

Tabs for information will be provided for "About, Features, Where to buy" - This information will be provided by us, once the webpage is complete.

Font is "Helvetica"
Nice to have
• Prepare the page flow so multiple variations of the product, and accessories can be added easily. As mentioned earlier, a shopping cart will be required (ShopTill) in the near future.

As you can see the company logo is designed to be cut into the product. It would be nice if it had an embossed effect to look the same. This goes for the "Talvex" logo also.

```html
<!DOCTYPE html>
<html lang="en">
<head>
<meta charset="utf-8">
<title>Orvane – Talvex Mobile</title>
<link rel="stylesheet" href="https://fonts.googleapis.com/css2?family=Arimo:wght@400;700&display=swap">
<style>
  :root {
    --stage: #2a2a2a;
    --metal-light: #ebebeb;
    --metal-mid: #d5d5d5;
    --metal-dark: #aaaaaa;
    --metal-deep: #919191;
    --ink: #111111;
    --rule: #5c5c5c;
    --bar: #000000;
    --white: #ffffff;
    --paper: #f6f6f6;
    --accent: #e8262b;
    --logo: #8a8a8a;
    --photo-sky: #c8c8c8;
    --photo-ground: #6b6660;
  }
  * { box-sizing: border-box; margin: 0; padding: 0; }
  html, body { width: 1200px; height: 1200px; overflow: hidden; }
  body {
    background: var(--stage);
    font-family: "Arimo", "Helvetica Neue", Helvetica, Arial, sans-serif;
  }
  .mobile-page {
    position: absolute;
    left: 280px;
    top: 140px;
    width: 640px;
    height: 920px;
    overflow: hidden;
    background: var(--white);
  }
  .site-header {
    height: 200px;
    background: linear-gradient(160deg, var(--metal-light) 0%, var(--metal-mid) 35%, var(--metal-dark) 60%, var(--metal-mid) 80%, var(--metal-light) 100%);
    display: flex;
    align-items: center;
    justify-content: center;
  }
  .brand-name {
    font-weight: 700;
    font-size: 78px;
    letter-spacing: 4px;
    color: var(--logo);
  }
  .cart-bar {
    height: 56px;
    background: var(--bar);
    display: flex;
    align-items: center;
    justify-content: flex-end;
    padding-right: 28px;
    gap: 14px;
  }
  .cart-label {
    color: var(--white);
    font-weight: 700;
    font-size: 23px;
  }
  .cart-count {
    position: relative;
    background: var(--accent);
    color: var(--white);
    font-weight: 700;
    font-size: 20px;
    height: 32px;
    min-width: 36px;
    padding: 0 8px 0 10px;
    line-height: 32px;
    text-align: center;
    border-radius: 3px;
  }
  .cart-count::before {
    content: "";
    position: absolute;
    left: -12px;
    top: 0;
    border-top: 16px solid transparent;
    border-bottom: 16px solid transparent;
    border-right: 12px solid var(--accent);
  }
  .main-nav {
    height: 330px;
    padding: 26px 34px 0 34px;
    background: linear-gradient(160deg, var(--metal-light) 0%, var(--metal-mid) 30%, var(--metal-dark) 55%, var(--metal-mid) 75%, var(--metal-light) 100%);
  }
  .nav-item {
    display: flex;
    justify-content: space-between;
    align-items: baseline;
    height: 67px;
    padding: 14px 10px 0 10px;
    border-bottom: 2px solid var(--rule);
    color: var(--ink);
    font-size: 46px;
    text-decoration: none;
    line-height: 1;
  }
  .nav-arrow {
    font-size: 36px;
  }
  .feature-area {
    height: 334px;
    padding: 20px 22px 14px 22px;
  }
  .video-card {
    border: 2px solid var(--metal-deep);
    height: 300px;
    position: relative;
    overflow: hidden;
  }
  .video-still {
    position: absolute;
    left: 0;
    top: 0;
    right: 0;
    bottom: 72px;
    background: linear-gradient(180deg, var(--photo-sky) 0%, #e2e2e2 45%, var(--photo-ground) 100%);
  }
  .play-button {
    position: absolute;
    left: 250px;
    top: 60px;
    width: 90px;
    height: 90px;
  }
  .video-caption {
    position: absolute;
    left: 0;
    bottom: 0;
    width: 100%;
    height: 72px;
    background: var(--white);
    padding: 8px 20px;
  }
  .caption-flag {
    display: block;
    color: var(--accent);
    font-weight: 700;
    font-size: 23px;
    line-height: 1.1;
  }
  .caption-title {
    display: block;
    color: var(--ink);
    font-size: 23px;
    line-height: 1.3;
    white-space: nowrap;
  }
  .product-shot {
    position: absolute;
    right: 12px;
    bottom: 8px;
    width: 130px;
    height: 104px;
    background: linear-gradient(135deg, #5c5c5c, #1c1c1c);
    border-radius: 8px;
  }
</style>
</head>
<body>
  <main class="mobile-page">
    <header class="site-header">
      <span class="brand-name">ORVANE</span>
    </header>
    <div class="cart-bar">
      <span class="cart-label">Shopping Cart</span>
      <span class="cart-count">0</span>
    </div>
    <nav class="main-nav">
      <a class="nav-item" href="#store"><span>STORE</span><span class="nav-arrow">&gt;</span></a>
      <a class="nav-item" href="#about"><span>ABOUT</span><span class="nav-arrow">&gt;</span></a>
      <a class="nav-item" href="#features"><span>FEATURES</span><span class="nav-arrow">&gt;</span></a>
      <a class="nav-item" href="#where-to-buy"><span>WHERE TO BUY</span><span class="nav-arrow">&gt;</span></a>
    </nav>
    <section class="feature-area">
      <div class="video-card">
        <div class="video-still" role="img" aria-label="Video still of riders in gear celebrating on a rocky hilltop"></div>
        <svg class="play-button" viewBox="0 0 94 94" aria-hidden="true">
          <rect width="94" height="94" rx="6" fill="rgba(0,0,0,0.55)"/>
          <polygon points="34,24 34,70 72,47" fill="#ffffff"/>
        </svg>
        <div class="video-caption">
          <span class="caption-flag">NEW</span>
          <span class="caption-title">K7100 HYDRAULIC CAMERA MOUNT</span>
        </div>
        <div class="product-shot" role="img" aria-label="Product photo of the black hydraulic camera mount"></div>
      </div>
    </section>
  </main>
</body>
</html>
```